Tariq Goldsmiths Stationary Contest

Pakistan’s largest Jewellery, Diamond and luxury watches store requires professional stationery. We have a long list of are trusted clients since 1959, our third generation has successfully maintained and sustained the legacy and excellence in the sector.

We require stationery template as part of this contest. The stationery can be double sided.

We prefer a design that makes use of some of the premium business stationery printing options, such as foil stamping, embossing/debossing, painted edges, spot UV etc (doesn't have to use all these options, only what you feel works, but we are looking for a design that stands out and is memorable and these nice touches have that effect.)

We want an eye catching, innovative, high end professional looking stationery for an out of box design that blends well with our new logo (attached). We want the design to be an out of box solution, you may use any element to compliment the logo. You may consider incorporating watermark etc, highlighting our products (Gold and Diamond Jewellery in addition to Luxury watches)

Company details are as follows;

Company name: Tariq Goldsmiths
Contact Person: Farhan Qureshi
Designation: Business Development Consultant
Mobile: +92 333 815 6042
Email: farhanqureshi@mailvale.com
Website: www.tariqgoldsmiths.com

Target Market(s)

Matrimonial, Elite & Businesses class, Upmarket

Font styles to use
Other font styles liked:
• Designers choice

Colors

Designer to choose colors to be used in the design.

Requirements
Must have
• Look and feel: Upmarket, innovative, Modern, Professional, graceful, Elegant, designer stuff.
Nice to have
• Unique design

```html
<!DOCTYPE html>
<html lang="en">
<head>
<meta charset="utf-8">
<title>Tariq Goldsmiths – Business Card</title>
<link rel="stylesheet" href="https://fonts.googleapis.com/css2?family=Montserrat:wght@300;400;600&display=swap">
<style>
  :root {
    --backdrop: #dedede;
    --card: #151515;
    --card-edge: #262626;
    --gold: #c9a27e;
    --gold-soft: #b48e6c;
  }
  * { margin: 0; padding: 0; box-sizing: border-box; }
  html, body { width: 1200px; height: 960px; overflow: hidden; }
  body {
    background: var(--backdrop);
    font-family: "Montserrat", sans-serif;
    color: var(--gold);
    position: relative;
  }
  .card {
    position: absolute;
    top: 326px;
    width: 540px;
    height: 308px;
    background: linear-gradient(135deg, var(--card) 55%, var(--card-edge));
    box-shadow: 0 6px 14px rgba(0,0,0,0.25);
  }
  .card--front { left: 40px; }
  .card--back { left: 620px; }

  .front-brand {
    position: absolute;
    left: 0; right: 0; top: 100px;
    text-align: center;
  }
  .brand-dot {
    display: block;
    width: 30px; height: 30px;
    margin: 0 auto 22px;
    border: 2px solid var(--gold);
    border-radius: 50%;
  }
  .brand-name {
    font-weight: 600;
    font-size: 20px;
    letter-spacing: 2px;
    text-transform: uppercase;
    color: var(--gold);
  }

  .back-brand {
    position: absolute;
    right: 40px; top: 74px;
    font-size: 18px;
  }
  .contact-person {
    position: absolute;
    left: 44px; top: 186px;
  }
  .person-name {
    font-weight: 600;
    font-size: 17px;
    letter-spacing: 1.5px;
    text-transform: uppercase;
  }
  .person-title {
    font-weight: 400;
    font-size: 12px;
    margin-top: 4px;
    letter-spacing: 0.3px;
  }
  .divider {
    position: absolute;
    left: 44px; right: 44px; top: 246px;
    height: 1px;
    background: var(--gold-soft);
  }
  .contact-line {
    position: absolute;
    left: 44px; right: 44px; top: 260px;
    font-weight: 300;
    font-size: 10.5px;
    white-space: nowrap;
    display: flex;
    justify-content: space-between;
  }
</style>
</head>
<body>
  <section class="card card--front" aria-label="Card front">
    <div class="front-brand">
      <span class="brand-dot"></span>
      <div class="brand-name">Tariq Goldsmiths</div>
    </div>
  </section>

  <section class="card card--back" aria-label="Card back">
    <div class="brand-name back-brand">Tariq Goldsmiths</div>
    <div class="contact-person">
      <div class="person-name">Farhan Qureshi</div>
      <div class="person-title">Business Development Consultant</div>
    </div>
    <div class="divider"></div>
    <div class="contact-line">
      <span>+92 333 815 6042</span><span>|</span>
      <span>farhanqureshi@mailvale.com</span><span>|</span>
      <span>www.tariqgoldsmiths.com</span>
    </div>
  </section>
</body>
</html>
```